Banners for website home page

I'm looking for 3 banners that will rotate on my website carousel addressing my 3 target markets. The website is Ledgerwise Harbor.

1) Young Starters
Headline: Start smart. Invest with confidence.
Sub: Learn the basics, set your first goal, and build a long-term plan with Ledgerwise Harbor.
CTA: Start free
Hero image ideas: Young person with phone/laptop; app UI overlay; subtle navy/gold chart shapes.

2) Saving for a Goal
Headline: Turn your goal into a plan.
Sub: Home deposit or child’s education—set targets, see projections, and track progress.
CTA: Plan my goal
Hero image ideas: Couple/family looking at house plans or a uni cap; progress bar overlay; warm light.

3) Retirement Fund Owners
Headline: Grow and protect your Retirement Fund.
Sub: Professional-grade tracking and signals to help your super grow—and last.
CTA: Start Now
Hero image ideas: Mature couple with tablet / beach walk; portfolio charts/compass motif overlaid.

Our app does the following:
Ledgerwise Harbor is an easy-to-use app designed to help everyday people take control of their investing journey.
Backed by over 10 years of proven investment models and experience, it empowers you to set realistic goals, build a tailored investment plan, and confidently manage your risk. With built-in education, alerts, and market insights, Ledgerwise Harbor helps you stay on course and maximise returns—no guesswork, just smart investing.

See attached an example AI generated banner and current logo to base colours, feel. for the website I use a dark blue menu and below would like a lighter colour - yellow/gold/white banner background.

Banner sizes : 1600 x 700 and 1200x525
Square size for mobile : 960x960 and 640x640
Format: WebP and PNG

```html
<!DOCTYPE html>
<html lang="en">
<head>
<meta charset="UTF-8">
<title>Ledgerwise Harbor – Start smart banner</title>
<link href="https://fonts.googleapis.com/css2?family=Poppins:wght@700&family=Urbanist:wght@400&display=swap" rel="stylesheet">
<style>
  :root {
    --navy: #141c47;
    --gold-deep: #c48a28;
    --gold-light: #f4ba5e;
    --white: #ffffff;
    --stage: #d2d3d5;
    --body-text: #2f2f35;
    --button-text: #3a3020;
  }
  html, body {
    margin: 0;
    padding: 0;
    width: 1200px;
    height: 627px;
    overflow: hidden;
    background: var(--stage);
  }
  .banner {
    position: absolute;
    left: 0;
    top: 51px;
    width: 1200px;
    height: 525px;
    background: var(--white);
    overflow: hidden;
  }
  .banner-shapes {
    position: absolute;
    inset: 0;
    width: 1200px;
    height: 525px;
  }
  .hero-photo {
    position: absolute;
    left: 653px;
    top: 22px;
    width: 333px;
    height: 503px;
    border-radius: 140px 140px 0 0;
    background: linear-gradient(180deg, #6a5144 0%, #8a8a8e 30%, #5d5d62 60%, #cdb494 100%);
  }
  .headline {
    position: absolute;
    left: 92px;
    top: 58px;
    margin: 0;
    font-family: "Poppins", sans-serif;
    font-weight: 700;
    font-size: 62px;
    line-height: 66px;
    letter-spacing: -0.5px;
    color: var(--navy);
  }
  .subline {
    position: absolute;
    left: 96px;
    top: 252px;
    width: 390px;
    margin: 0;
    font-family: "Urbanist", sans-serif;
    font-weight: 400;
    font-size: 22px;
    line-height: 36px;
    color: var(--body-text);
  }
  .cta {
    position: absolute;
    left: 115px;
    top: 380px;
    width: 174px;
    height: 46px;
    border-radius: 23px;
    background: linear-gradient(90deg, var(--gold-deep), var(--gold-light) 55%, var(--gold-deep));
    font-family: "Poppins", sans-serif;
    font-weight: 700;
    font-size: 24px;
    line-height: 46px;
    text-align: center;
    color: var(--button-text);
    text-decoration: none;
  }
</style>
</head>
<body>
  <section class="banner">
    <svg class="banner-shapes" viewBox="0 0 1200 525" aria-hidden="true">
      <defs>
        <radialGradient id="gold-glow" cx="50%" cy="45%" r="60%">
          <stop offset="0%" stop-color="#ffc46a"/>
          <stop offset="100%" stop-color="#c48a28"/>
        </radialGradient>
        <linearGradient id="gold-sweep" x1="0" y1="0" x2="1" y2="1">
          <stop offset="0%" stop-color="#c48a28"/>
          <stop offset="50%" stop-color="#f2b558"/>
          <stop offset="100%" stop-color="#c48a28"/>
        </linearGradient>
      </defs>
      <path class="corner-navy-left" d="M0 0 H195 C110 25 40 70 0 122 Z" fill="#141c47"/>
      <path class="corner-navy-right" d="M1009 0 H1200 V122 C1160 60 1090 20 1009 0 Z" fill="#141c47"/>
      <path class="corner-gold-left" d="M0 409 C40 470 110 510 191 525 H0 Z" fill="url(#gold-sweep)"/>
      <ellipse class="gold-cap" cx="536" cy="10" rx="120" ry="54" fill="url(#gold-glow)"/>
      <path class="hero-blob" d="M476 401 C476 330 560 300 653 236 C730 180 780 110 870 110 C960 110 1010 170 1070 230 C1130 280 1170 330 1170 401 C1170 460 1140 500 1100 525 H578 C520 490 476 450 476 401 Z" fill="#141c47"/>
      <circle cx="1054" cy="143" r="41" fill="url(#gold-glow)"/>
      <circle cx="1110" cy="109" r="5" fill="#141c47"/>
      <circle cx="392" cy="373" r="21" fill="url(#gold-glow)"/>
      <circle cx="388" cy="455" r="28" fill="#141c47"/>
    </svg>

    <div class="hero-photo" role="img" aria-label="Photo of a young man in glasses and a blazer holding a phone and a laptop, in front of a navy and gold compass motif"></div>

    <h1 class="headline">Start smart<br>Invest with<br>confidence</h1>
    <p class="subline">Learn the basics, set your first goal, and build a long-term plan with Ledgerwise Harbor.</p>
    <a class="cta" href="#">Start free</a>
  </section>
</body>
</html>
```